Maple Ridge business card design

Card needs to include the following text/items:
Company Logo
Rupert Hollis
Phone # - 517-386-9042
service@mapleridgelandscaping.example
Lawn & landscape maintenance services

```html
<!DOCTYPE html>
<html lang="en">
<head>
<meta charset="utf-8">
<title>Maple Ridge business card</title>
<link href="https://fonts.googleapis.com/css2?family=Cinzel:wght@700&family=Montserrat:wght@400;700&family=Tinos&display=swap" rel="stylesheet">
<style>
  :root {
    --backdrop: #e6e6e6;
    --card: #ffffff;
    --forest: #1a4a0a;
    --band: #133f00;
    --ink: #222222;
    --rule: #333333;
    --mark: #6db33f;
  }
  * { margin: 0; padding: 0; box-sizing: border-box; }
  html, body { width: 1014px; height: 1200px; overflow: hidden; }
  body { background: var(--backdrop); position: relative; font-family: "Montserrat", sans-serif; }
  .card {
    position: absolute; left: 61px; width: 884px; height: 505px;
    background: var(--card);
    box-shadow: 0 10px 24px rgba(0,0,0,0.18);
  }
  .card--front { top: 59px; }
  .card--back { top: 604px; }
  .brand { position: absolute; text-align: center; }
  .brand__circle { display: block; margin: 0 auto; border-radius: 50%; background: var(--mark); }
  .brand__name { font-family: "Cinzel", serif; font-weight: 700; color: var(--forest); line-height: 1; white-space: nowrap; }
  .card--front .brand { left: 560px; top: 30px; width: 254px; }
  .card--front .brand__circle { width: 150px; height: 150px; }
  .card--front .brand__name { font-size: 38px; margin-top: 24px; }
  .card--back .brand { left: 0; width: 884px; top: 52px; }
  .card--back .brand__circle { width: 300px; height: 300px; }
  .card--back .brand__name { font-size: 66px; margin-top: 40px; }
  .person { position: absolute; left: 44px; top: 270px; }
  .person__name { font-family: "Cinzel", serif; font-weight: 700; font-size: 37px; color: var(--forest); line-height: 1; }
  .person__role { font-size: 23px; color: var(--ink); margin-top: 8px; }
  .rule { position: absolute; left: 50px; top: 367px; width: 787px; height: 2px; background: var(--rule); }
  .contact { position: absolute; left: 44px; list-style: none; display: flex; align-items: center; gap: 14px; color: var(--ink); }
  .contact svg { width: 22px; height: 22px; fill: var(--forest); }
  .contact--phone { top: 380px; font-family: "Tinos", serif; font-size: 25px; }
  .contact--email { top: 418px; font-size: 22px; }
  .tagline {
    position: absolute; left: 0; bottom: 0; width: 884px; height: 36px;
    background: var(--band); color: #fff; font-weight: 700; font-size: 22px;
    display: flex; align-items: center; justify-content: center;
  }
</style>
</head>
<body>
  <section class="card card--front">
    <div class="brand">
      <span class="brand__circle"></span>
      <div class="brand__name">Maple Ridge</div>
    </div>
    <div class="person">
      <h1 class="person__name">Rupert Hollis</h1>
      <p class="person__role">Managing Director</p>
    </div>
    <div class="rule"></div>
    <div class="contact contact--phone">
      <svg viewBox="0 0 24 24" aria-hidden="true"><path d="M6.6 10.8a15.1 15.1 0 0 0 6.6 6.6l2.2-2.2a1 1 0 0 1 1-.25 11.4 11.4 0 0 0 3.6.57 1 1 0 0 1 1 1V20a1 1 0 0 1-1 1A17 17 0 0 1 3 4a1 1 0 0 1 1-1h3.5a1 1 0 0 1 1 1c0 1.25.2 2.45.57 3.6a1 1 0 0 1-.25 1z"/></svg>
      <span>517-386-9042</span>
    </div>
    <div class="contact contact--email">
      <svg viewBox="0 0 24 24" aria-hidden="true"><path d="M2 5h20v14H2z M3.5 6.5 12 13l8.5-6.5" fill="var(--forest)" stroke="#fff" stroke-width="1.4"/></svg>
      <span>service@mapleridgelandscaping.example</span>
    </div>
    <div class="tagline">Lawn &amp; landscape maintenance services</div>
  </section>

  <section class="card card--back">
    <div class="brand">
      <span class="brand__circle"></span>
      <div class="brand__name">Maple Ridge</div>
    </div>
  </section>
</body>
</html>
```